Poster to advertise new mind coaching clinic

Create a single sided A4 colour poster using the text provided. Suggested image provided. You may want to suggest an alternative however images need to appeal to both male and female sports people.

Text:
One-to-one mind coaching
For recreational and competitive sports people
Learn the mental tools and techniques used by the top sports people to fulfil your potential

 Create well-formed and achievable goals
 Overcome limiting beliefs
 Accelerate mastery through modelling your heroes
 Learn how to use mental rehearsal to increase your chances of success
 Smash through belief ceilings
 Get into the zone to bring your ‘Best Game’ more often
Thursdays in central Ashcombe
5-8pm
For more information contact:
thebluekitecoaching@postmere.com
Tel: 07481 265314
www.the-blue-kite.co.uk

Target Market(s)

sports people

Industry/Entity Type

Clinic

Requirements
Must have
• All the content provided. Contact details.

```html
<!DOCTYPE html>
<html lang="en">
<head>
<meta charset="utf-8">
<title>One-to-One Mind Coaching Poster</title>
<link href="https://fonts.googleapis.com/css2?family=League+Spartan:wght@800;900&family=Jost:wght@700&family=Lato:wght@700;900&display=swap" rel="stylesheet">
<style>
  :root {
    --backdrop: #e6e7e8;
    --frame-blue: #118dc8;
    --cream: #fff6a8;
    --ink: #231f20;
    --accent-blue: #1a8fc9;
    --white: #ffffff;
    --track-blue: #2f86c9;
    --track-deep: #1c5f9c;
  }
  * { box-sizing: border-box; margin: 0; padding: 0; }
  html, body {
    width: 1200px; height: 1172px; overflow: hidden;
    background: var(--backdrop);
  }
  .poster {
    position: absolute; left: 210px; top: 36px;
    width: 779px; height: 1100px;
    background: var(--frame-blue);
  }
  .panel {
    position: absolute; left: 51px; top: 49px;
    width: 678px; height: 1002px;
    background: var(--cream);
    border-radius: 10px;
    overflow: hidden;
  }
  .headline {
    position: absolute; top: 54px; left: 0; width: 100%;
    text-align: center;
    font-family: "League Spartan", sans-serif;
    font-weight: 900;
    font-size: 82px; line-height: 68px;
    letter-spacing: -1px;
    color: var(--ink);
    text-transform: uppercase;
  }
  .audience {
    position: absolute; top: 262px; left: 0; width: 100%;
    text-align: center;
    font-family: "Jost", sans-serif;
    font-weight: 700;
    font-size: 32.5px; line-height: 31px;
    color: var(--accent-blue);
    text-transform: uppercase;
  }
  .intro {
    position: absolute; top: 342px; left: 0; width: 100%;
    text-align: center;
    font-family: "Lato", sans-serif;
    font-weight: 900;
    font-size: 24px; line-height: 26px;
    color: var(--ink);
  }
  .hero-photo {
    position: absolute; top: 411px; left: 0;
    width: 100%; height: 354px;
    background: linear-gradient(160deg, var(--track-blue) 0%, #3a93d4 45%, var(--track-deep) 100%);
  }
  .benefits {
    position: absolute; top: 772px; left: 0; width: 100%;
    list-style: none;
    text-align: center;
    font-family: "Lato", sans-serif;
    font-weight: 700;
    font-size: 14.9px; line-height: 18.2px;
    color: var(--ink);
  }
  .benefits .dot { color: var(--accent-blue); margin: 0 3px 0 6px; }
  .footer {
    position: absolute; top: 869px; left: 0;
    width: 100%; height: 133px;
    background: var(--white);
  }
  .brand {
    position: absolute; left: 60px; top: 44px;
    display: flex; align-items: center; gap: 12px;
    font-family: "Lato", sans-serif;
    font-weight: 900;
    font-size: 30px;
    color: var(--ink);
  }
  .brand-mark {
    width: 34px; height: 34px; border-radius: 50%;
    background: var(--accent-blue);
  }
  .divider {
    position: absolute; left: 323px; top: 12px;
    width: 1.5px; height: 105px; background: var(--ink);
  }
  .contact {
    position: absolute; left: 341px; top: 7px;
    font-family: "Lato", sans-serif;
    font-weight: 700;
    font-size: 16px;
    color: var(--ink);
  }
  .contact .schedule { line-height: 20px; margin-bottom: 8px; }
  .contact .cta {
    display: inline-block;
    background: var(--cream);
    padding: 0 8px 0 22px;
    line-height: 19px; margin-bottom: 1px;
  }
  .contact .line { display: flex; align-items: center; gap: 5px; line-height: 22px; }
  .contact svg { width: 9px; height: 9px; flex: none; }
</style>
</head>
<body>
  <div class="poster">
    <div class="panel">
      <h1 class="headline">One-to-One<br>Mind<br>Coaching</h1>
      <p class="audience">For recreational and<br>competitive sports people</p>
      <p class="intro">Learn the mental tools and techniques used by<br>the top sports people to fulfil your potential</p>

      <div class="hero-photo" role="img" aria-label="Photo of a sprinter crossing the finish line on a blue indoor track, arms raised in celebration"></div>

      <ul class="benefits">
        <li><span class="dot">•</span>Create well-formed and achievable goals <span class="dot">•</span> Overcome limiting beliefs</li>
        <li><span class="dot">•</span>Accelerate mastery through modelling your heroes</li>
        <li><span class="dot">•</span>Learn how to use mental rehearsal to increase your chances of success</li>
        <li><span class="dot">•</span>Smash through belief ceilings <span class="dot">•</span> Get into the zone to bring your ‘Best Game’ more often</li>
      </ul>

      <div class="footer">
        <div class="brand"><span class="brand-mark"></span>The Blue Kite</div>
        <div class="divider"></div>
        <div class="contact">
          <p class="schedule">Thursdays in central Ashcombe - 5-8 pm</p>
          <p class="cta">For more information contact:</p>
          <p class="line">
            <svg viewBox="0 0 10 10"><circle cx="5" cy="5" r="4" fill="none" stroke="#231f20" stroke-width="1.2"/><circle cx="5" cy="5" r="1.5" fill="#231f20"/></svg>
            thebluekitecoaching@postmere.com
          </p>
          <p class="line">
            <svg viewBox="0 0 10 10"><rect x="0.5" y="2" width="9" height="6.5" fill="#231f20"/><path d="M0.8 2.4 L5 5.8 L9.2 2.4" fill="none" stroke="#fff" stroke-width="0.9"/></svg>
            Tel: 07481 265314
          </p>
          <p class="line">
            <svg viewBox="0 0 10 10"><circle cx="5" cy="5" r="4.3" fill="#231f20"/><path d="M0.8 5 H9.2 M5 0.8 V9.2" stroke="#fff" stroke-width="0.7"/></svg>
            www.the-blue-kite.co.uk
          </p>
        </div>
      </div>
    </div>
  </div>
</body>
</html>
```